Flyers for social media company

To create a postcard sized flyer to send to potential clients informing them of our business and what we can offer.

We are a social media company offering clients web design, social media management on a number of platforms.

Would be nice to have our Bright Wren surrounded by a number of yellow ducks so the blue stand out from the crowd.

Industry/Entity Type

Business

```html
<!DOCTYPE html>
<html lang="en">
<head>
<meta charset="utf-8">
<title>Bright Wren – Postcard Flyer</title>
<link rel="stylesheet" href="https://fonts.googleapis.com/css2?family=Raleway:wght@300;400;500;600&display=swap">
<style>
  :root{
    --stage:#a9a9a9;
    --ink:#231f20;
    --sky:#29a9e1;
    --azure:#0c8fdb;
    --royal:#1b3f9e;
    --navy:#1a2f86;
    --white:#ffffff;
    --rule:#9a9a9a;
    --sun:#f6d80c;
  }
  *{margin:0;padding:0;box-sizing:border-box}
  html,body{width:720px;height:1200px;overflow:hidden}
  body{background:var(--stage);font-family:"Raleway",sans-serif;position:relative}
  .card{position:absolute;left:53px;width:614px;height:397px;overflow:hidden;box-shadow:0 3px 8px rgba(0,0,0,.35)}
  .card-front{top:180px}
  .card-back{top:623px;background:var(--white)}
  .card svg.shapes{position:absolute;inset:0;width:100%;height:100%}
  .abs{position:absolute}

  /* front */
  .front-brand{left:39px;top:301px;display:flex;align-items:center;gap:14px}
  .brand-dot{width:66px;height:66px;border-radius:50%;background:var(--sky);flex:none}
  .front-name{font-size:37px;font-weight:400;color:var(--sky);line-height:1;letter-spacing:.5px}
  .front-sub{font-size:12.5px;font-weight:500;color:var(--white);letter-spacing:.6px;margin-top:3px}
  .front-web{right:26px;top:354px;font-size:12.5px;color:var(--white);white-space:nowrap}
  .front-web b{color:var(--sky);font-weight:600}
  .globe{display:inline-block;width:9px;height:9px;border-radius:50%;background:var(--sky);margin-right:6px;vertical-align:0}

  /* back */
  .back-brand{left:0;width:334px;top:142px;text-align:center;color:var(--white)}
  .back-name{font-size:27px;font-weight:400;line-height:1}
  .back-sub{font-size:9.5px;font-weight:500;letter-spacing:.4px;margin-top:1px}
  .back-tagline{font-size:17px;font-weight:600;margin-top:3px}
  .service{top:296px;width:160px;text-align:center;color:var(--white);font-size:12px;line-height:1.25}
  .service-web{left:0}
  .service-social{left:162px}
  .back-web{left:0;width:334px;top:364px;text-align:center;color:var(--white);font-size:11px;letter-spacing:5px}
  .address-brand{left:354px;top:35px;display:flex;align-items:center;gap:5px}
  .address-brand .brand-dot{width:40px;height:40px}
  .address-name{font-size:17px;color:var(--sky);line-height:1}
  .address-sub{font-size:6px;font-weight:600;color:var(--ink);letter-spacing:.2px;margin-top:1px}
  .stamp-box{left:524px;top:20px;width:76px;height:72px;border:1px solid var(--rule)}
  .address-line{left:340px;width:254px;height:1px;background:var(--rule)}
</style>
</head>
<body>

<section class="card card-front">
  <svg class="shapes" viewBox="0 0 614 397" preserveAspectRatio="none">
    <defs>
      <radialGradient id="crowd" cx="0.62" cy="0.32" r="0.75" fx="0.62" fy="0.32">
        <stop offset="0" stop-color="#1f6fc4"/>
        <stop offset=".14" stop-color="#3d8ad8"/>
        <stop offset=".24" stop-color="#f3e27a"/>
        <stop offset=".45" stop-color="#f6d80c"/>
        <stop offset=".75" stop-color="#f9e564"/>
        <stop offset="1" stop-color="#fdf3b8"/>
      </radialGradient>
    </defs>
    <polygon role="img" aria-label="Photo of a blue rubber duck standing out among many yellow rubber ducks" fill="url(#crowd)" points="0,0 614,0 614,262 470,287 0,240"/>
    <polygon fill="var(--azure)" points="0,240 470,287 614,262 614,290 0,290"/>
    <rect fill="var(--ink)" x="0" y="290" width="614" height="107"/>
    <polygon fill="var(--royal)" points="400,290 614,290 614,330"/>
  </svg>
  <div class="abs front-brand">
    <span class="brand-dot"></span>
    <div>
      <div class="front-name">BRIGHT WREN</div>
      <div class="front-sub">SOCIAL MEDIA MANAGEMENT</div>
    </div>
  </div>
  <div class="abs front-web"><span class="globe"></span>www.<b>brightwren</b>.com</div>
</section>

<section class="card card-back">
  <svg class="shapes" viewBox="0 0 614 397" preserveAspectRatio="none">
    <defs>
      <linearGradient id="panel" x1="0" y1="0" x2="0" y2="1">
        <stop offset="0" stop-color="#1aa6e4"/>
        <stop offset=".55" stop-color="#0d6fc9"/>
        <stop offset="1" stop-color="#1a2f86"/>
      </linearGradient>
      <linearGradient id="team" x1="0" y1="0" x2="0" y2="1">
        <stop offset="0" stop-color="#ffffff" stop-opacity=".22"/>
        <stop offset="1" stop-color="#ffffff" stop-opacity="0"/>
      </linearGradient>
    </defs>
    <rect fill="url(#panel)" x="0" y="0" width="334" height="397"/>
    <rect role="img" aria-label="Faint overhead photo of a team working at a desk" fill="url(#team)" x="0" y="0" width="282" height="190"/>
    <polygon fill="var(--royal)" points="282,0 333,0 333,397 330,397"/>
    <polygon fill="var(--ink)" points="332,0 336,0 360,397 330,397"/>
    <line x1="158" y1="220" x2="158" y2="318" stroke="#ffffff" stroke-opacity=".4" stroke-width="1"/>
    <g fill="none" stroke="#fff" stroke-width="1.6">
      <rect x="60" y="232" width="44" height="32" rx="2"/>
      <line x1="82" y1="264" x2="82" y2="272"/>
      <line x1="72" y1="273" x2="92" y2="273"/>
      <rect x="66" y="238" width="14" height="11"/>
      <line x1="85" y1="241" x2="98" y2="241"/>
      <line x1="85" y1="246" x2="98" y2="246"/>
      <line x1="66" y1="254" x2="98" y2="254"/>
    </g>
    <g fill="none" stroke="#fff" stroke-width="1.6">
      <circle cx="248" cy="238" r="8"/>
      <path d="M232 262 q0-14 16-14 q16 0 16 14 z"/>
      <circle cx="236" cy="242" r="7"/>
      <path d="M222 264 q0-12 14-12"/>
    </g>
  </svg>

  <div class="abs back-brand">
    <div class="back-name">BRIGHT WREN</div>
    <div class="back-sub">SOCIAL MEDIA MANAGEMENT</div>
    <div class="back-tagline">We are a social media company</div>
  </div>
  <div class="abs service service-web">web design</div>
  <div class="abs service service-social">social media<br>management</div>
  <div class="abs back-web">www.brightwren.com</div>

  <div class="abs address-brand">
    <span class="brand-dot"></span>
    <div>
      <div class="address-name">BRIGHT WREN</div>
      <div class="address-sub">SOCIAL MEDIA MANAGEMENT</div>
    </div>
  </div>
  <div class="abs stamp-box"></div>
  <div class="abs address-line" style="top:163px"></div>
  <div class="abs address-line" style="top:199px"></div>
  <div class="abs address-line" style="top:235px"></div>
  <div class="abs address-line" style="top:271px"></div>
</section>

</body>
</html>
```